Redesign Login page

I want to redesign my login page to bring my 2 products closer together. I am only looking to redesign one login page, not 2.

For the logo, please make it solid and it can be black or white if helpful. I can also fine tune the logo if you get it close.

Coding

Coded - Design and coding required

Number of Pages Required

1 page

```html
<!DOCTYPE html>
<html lang="en">
<head>
<meta charset="utf-8">
<title>NorthView – Sign in</title>
<link rel="stylesheet" href="https://fonts.googleapis.com/css2?family=Cabin:wght@400;500;600;700&family=Figtree:wght@400;500;600&display=swap">
<style>
  :root{
    --ink:#02403e;
    --teal:#86d5cf;
    --teal-text:#5aa9a0;
    --field:#e8f0fe;
    --page:#ffffff;
    --rule:#8fb9b5;
  }
  *{box-sizing:border-box;margin:0;padding:0}
  html,body{width:1200px;height:817px;overflow:hidden;background:var(--page)}
  body{position:relative;font-family:"Cabin",sans-serif;color:var(--ink)}

  .login-card{
    position:absolute;left:365px;top:130px;width:470px;height:556px;
    border:3px solid var(--teal);border-radius:22px;background:#fff;
    box-shadow:0 0 10px rgba(134,213,207,.55),0 6px 14px rgba(2,64,62,.18);
  }
  .welcome{position:absolute;left:0;right:0;top:28px;text-align:center;font-size:23px;letter-spacing:.5px}
  .brand-name{position:absolute;left:0;right:0;top:52px;text-align:center;font-size:54px;font-weight:700;letter-spacing:-1px;line-height:1}

  .field{
    position:absolute;left:44px;width:372px;height:46px;border:2px solid var(--teal);
    border-radius:23px;background:var(--field);display:flex;align-items:center;padding-left:22px;
    box-shadow:0 2px 3px rgba(2,64,62,.12);font-size:15px;
  }
  .field svg{flex:none;margin-right:9px}
  .field-email{top:140px}
  .field-password{top:199px}
  .toggle-visibility{position:absolute;right:20px;top:13px}

  .continue-btn{
    position:absolute;left:45px;top:267px;width:371px;height:43px;border-radius:22px;background:var(--ink);
    color:#fff;font-family:"Figtree",sans-serif;font-weight:600;font-size:17px;display:flex;align-items:center;justify-content:center;
  }
  .remember{position:absolute;left:50px;top:323px;display:flex;align-items:center;font-size:14px;letter-spacing:.3px}
  .checkbox{width:14px;height:14px;border-radius:3px;background:var(--ink);margin-right:7px;display:flex;align-items:center;justify-content:center}
  .forgot{position:absolute;right:56px;top:320px;font-size:14px;letter-spacing:.3px}
  .signup{position:absolute;left:0;right:0;top:355px;text-align:center;font-size:14px;letter-spacing:.2px}
  .signup a{color:var(--teal-text);font-weight:600;text-decoration:none}

  .divider{position:absolute;left:67px;top:397px;width:337px;display:flex;align-items:center;gap:8px;
    font-family:"Figtree",sans-serif;font-size:11px;letter-spacing:.3px}
  .divider span.line{flex:1;height:1px;background:linear-gradient(90deg,transparent,var(--rule))}
  .divider span.line.right{background:linear-gradient(90deg,var(--rule),transparent)}

  .sso-btn{
    position:absolute;left:149px;width:167px;height:39px;border:1.5px solid var(--teal);border-radius:20px;background:#fff;
    display:flex;align-items:center;justify-content:center;gap:6px;font-family:"Figtree",sans-serif;font-size:15px;
    box-shadow:0 2px 3px rgba(2,64,62,.12);
  }
  .sso-orbit{top:429px}
  .sso-tessera{top:483px}
  .mark-circle{width:11px;height:11px;border-radius:50%;background:var(--ink)}
  .mark-square{width:11px;height:11px;background:var(--ink)}

  .site-footer{position:absolute;left:0;right:0;top:780px;display:flex;justify-content:center;align-items:baseline;gap:5px;font-size:8.5px}
  .footer-brand{font-size:14px;font-weight:700;letter-spacing:-.3px}
  .footer-contact{font-weight:700}
</style>
</head>
<body>
  <main class="login-card">
    <p class="welcome">Welcome to</p>
    <h1 class="brand-name">NorthView</h1>

    <div class="field field-email">
      <svg width="17" height="13" viewBox="0 0 17 13" fill="none" stroke="#86d5cf" stroke-width="1.1"><rect x=".6" y=".6" width="15.8" height="11.8"/><path d="M.6 .6 8.5 7.5 16.4 .6M.6 12.4 6.5 6M16.4 12.4 10.5 6"/></svg>
      <span>Email</span>
    </div>

    <div class="field field-password">
      <svg width="13" height="17" viewBox="0 0 13 17" fill="none" stroke="#86d5cf" stroke-width="1.2"><rect x=".8" y="7" width="11.4" height="9.2" rx="1.5"/><path d="M3 7V4.5a3.5 3.5 0 0 1 7 0V7"/><path d="M6.5 10.5v2.5" stroke-width="1.6"/></svg>
      <span>Password</span>
      <svg class="toggle-visibility" width="21" height="14" viewBox="0 0 21 14" fill="none" stroke="#86d5cf" stroke-width="1.3"><path d="M1 7c2.5-4 6-5.5 9.5-5.5S17.5 3 20 7c-2.5 4-6 5.5-9.5 5.5S3.5 11 1 7z"/><circle cx="10.5" cy="7" r="3" fill="#86d5cf"/><path d="M3 1.5 18.5 12.5"/></svg>
    </div>

    <div class="continue-btn">Continue</div>

    <div class="remember">
      <span class="checkbox"><svg width="10" height="8" viewBox="0 0 10 8" fill="none" stroke="#fff" stroke-width="1.8"><path d="M1 4l2.8 2.8L9 1"/></svg></span>
      Remember Me
    </div>
    <div class="forgot">Forgot Password?</div>

    <p class="signup">Don’t have an account ? <a href="#">Create an account</a></p>

    <div class="divider"><span class="line"></span>OR CONTINUE WITH<span class="line right"></span></div>

    <div class="sso-btn sso-orbit"><span class="mark-circle"></span>Orbit SSO</div>
    <div class="sso-btn sso-tessera"><span class="mark-square"></span>Tessera SSO</div>
  </main>

  <footer class="site-footer">
    <span class="footer-brand">NorthView</span>
    <span>© Lumen Ridge Partners.</span>
    <span class="footer-contact">Contact Us</span>
  </footer>
</body>
</html>
```